Zielgruppe
Wir sind eine Event-Agentur im Westen Berlins mit dem Teilschwerpunkt 'Medizin'. Zu unseren Kunden gehören namenhafte Krankenhäuser, Ärzte und Organisationen welche Fortbildungsveranstaltungen bei uns organisieren lassen. Unsere Zielgruppe sind Ärzte und medizinisches Personal, welche an unseren Events teilnehmen um auf dem neusten Stand der Medizin, Hygiene und anderen Themen zu bleiben.
Aufgabenstellung
UPDATE: Unser Chef wünscht sich, dass der Fokus nicht nur auf dem Thema Arthroskopie liegt, sondern schon eher in Richtung 'Gelenke' gehen soll. Bitte entsprechend beachten!
Wir benötigen ein Design für einen DIN lang Flyer, welches gleichzeitig modern und doch nicht zu flippig ist. Das Design muss den Spagat zwischen Technik und Menschlichkeit widerspiegeln. Farblich sind keine Vorgaben vorhanden. Ob mit Stock Fotos, graphischen Elementen oder mit typographischem Design: wir sind für alle Vorschläge offen.
Thematisch geht es um die Bewerbung einer Veranstaltung im orthopädischen Sektor (falls für Ihr Design relevant: es handelt sich um Arthroskopien). Das Design soll so angelegt sein, dass es im nächsten Jahr abgewandelt wiederverwendet werden kann ohne dass der Wiedererkennungswert verloren geht.
Folgende Texte müssen vorhanden sein:
'Veltrana-Symposium 2019' (Name der Veranstaltung)
'Neues aus der Schulter- und Kniearthroskopie' (Thema der Veranstaltung)
'21. bis 23. Februar 2019' (Datum)
'Krankenhaus Berlin' (Ort, leider noch mit Platzhalter)
Nice To Have, aber kein Muss: die Jahreszahl des jeweiligen Jahres könnte immer an der gleichen Stelle erscheinen. Für die nächste VA stünde dort 2019, aber für das darauffolgende Jahr 2020. Allerdings nur ein Gedanke von uns und kein Pflichtelement. Lieber nicht nutzen, falls es das Design irgendwie beeinträchtigt.
Falls Stockbilder dann bitte im erschwinglichen Rahmen vorschlagen! Das schönste Bild hilft uns nicht wenn es 50€ für 200x200 px kostet ;)
Vielen Dank im Voraus für Ihre Vorschläge!

```html
<!DOCTYPE html>
<html lang="de">
<head>
<meta charset="utf-8">
<title>Veltrana-Symposium 2019 – DIN lang Flyer</title>
<link href="https://fonts.googleapis.com/css2?family=Ubuntu:wght@400;500;700&family=Ubuntu+Condensed&family=Roboto:wght@700&display=swap" rel="stylesheet">
<style>
  :root {
    --page: #e8e8ee;
    --ink-dark: #1b1a38;
    --band-grey: #3b3b3e;
    --paper: #f4f4f9;
    --navy: #2a2e74;
    --white: #ffffff;
    --text-dark: #1a1a1a;
  }
  * { margin: 0; padding: 0; box-sizing: border-box; }
  html, body { width: 849px; height: 1200px; overflow: hidden; }
  body {
    background: var(--page);
    font-family: "Ubuntu", sans-serif;
    position: relative;
  }
  .flyer {
    position: absolute;
    top: 180px;
    width: 396px;
    height: 839px;
    background: var(--paper);
    overflow: hidden;
    box-shadow: 0 4px 14px rgba(0,0,0,0.18);
  }
  .flyer--front { left: 16px; }
  .flyer--back { left: 437px; }

  .top-band {
    position: absolute; left: 0; top: 0; width: 100%; height: 27px;
    background: var(--ink-dark);
  }
  .bottom-band {
    position: absolute; left: 0; bottom: 0; width: 100%; height: 21px;
    background: var(--band-grey);
  }
  .year-divider {
    position: absolute; left: 0; top: 290px; width: 100%; height: 30px;
  }
  .year-divider svg { position: absolute; left: 0; top: 0; }
  .year-label {
    position: absolute; right: 36px; top: 3px;
    font-family: "Roboto", sans-serif; font-weight: 700;
    font-size: 18px; color: var(--white);
  }

  /* Front */
  .front-head {
    position: absolute; left: 0; top: 27px; width: 100%; height: 263px;
    background: var(--paper);
  }
  .event-title {
    position: absolute; left: 38px; top: 113px;
    font-weight: 400; font-size: 28px; line-height: 33px;
    color: var(--navy);
  }
  .event-topic {
    position: absolute; left: 34px; top: 195px;
    height: 22px; padding: 0 5px;
    background: var(--band-grey); color: var(--white);
    font-family: "Ubuntu Condensed", sans-serif;
    font-size: 13.5px; line-height: 22px; white-space: nowrap;
  }
  .joint-visual {
    position: absolute; left: 0; top: 320px; width: 100%; height: 498px;
    background:
      radial-gradient(ellipse 30% 22% at 62% 40%, rgba(196,90,80,0.75), transparent 70%),
      radial-gradient(ellipse 45% 60% at 55% 45%, rgba(210,195,215,0.45), transparent 75%),
      linear-gradient(160deg, #15163a 0%, #262a5c 45%, #141533 100%);
  }
  .date-badge {
    position: absolute; left: 19px; top: 562px;
    width: 164px; height: 164px; border-radius: 50%;
    background: var(--navy); color: var(--white);
    text-align: center;
    display: flex; flex-direction: column; justify-content: center;
  }
  .date-badge__dates {
    font-family: "Roboto", sans-serif; font-weight: 700;
    font-size: 24px; line-height: 28px;
  }
  .date-badge__name {
    font-size: 15px; margin-top: 3px;
  }

  /* Back */
  .photo-grid {
    position: absolute; left: 0; top: 30px; width: 100%; height: 278px;
  }
  .photo {
    position: absolute;
  }
  .photo--hand-light { left: 0; top: 0; width: 200px; height: 139px;
    background: linear-gradient(120deg, #f7f4f3 0%, #eee4e1 60%, #e2ccc7 100%); }
  .photo--glove { left: 205px; top: 0; width: 191px; height: 139px;
    background: linear-gradient(135deg, #6e6a7c 0%, #8c8597 50%, #5e5b6c 100%); }
  .photo--syringe { left: 0; top: 144px; width: 200px; height: 134px;
    background: linear-gradient(160deg, #8e8b98 0%, #767382 100%); }
  .photo--shoulder { left: 205px; top: 144px; width: 191px; height: 134px;
    background: linear-gradient(135deg, #f6e2da 0%, #efd0c4 55%, #e9c5b7 100%); }
  .back-heading {
    position: absolute; left: 23px; top: 72px;
    font-size: 17px; line-height: 20px;
  }
  .back-heading__kind { font-weight: 700; color: var(--text-dark); }
  .back-heading__name { font-weight: 400; color: var(--navy); margin-top: 3px; }

  .joint-visual--soft {
    position: absolute; left: 0; top: 320px; width: 100%; height: 498px;
    background:
      radial-gradient(ellipse 35% 45% at 55% 30%, rgba(215,212,222,0.7), transparent 75%),
      linear-gradient(180deg, #ecebf0 0%, #f7f7fa 50%, #efeff3 100%);
  }
  .topic-badge {
    position: absolute; left: 29px; top: 257px;
    width: 152px; height: 152px; border-radius: 50%;
    background: var(--ink-dark); color: var(--white);
    display: flex; align-items: center; justify-content: center;
    text-align: center;
    font-size: 16px; line-height: 19px;
  }
  .teaser {
    position: absolute; left: 0; top: 485px; width: 100%;
    text-align: center; color: var(--navy);
    font-size: 19.5px; line-height: 25px;
  }
  .teaser__lead { color: var(--text-dark); font-size: 23px; line-height: 27px; }
  .info-band {
    position: absolute; left: 0; top: 650px; width: 100%; height: 79px;
    background: var(--ink-dark); color: var(--white);
    font-family: "Ubuntu Condensed", sans-serif;
    font-size: 17px; line-height: 24px; text-align: center;
    display: flex; flex-direction: column; justify-content: center;
  }
</style>
</head>
<body>

<section class="flyer flyer--front" aria-label="Vorderseite">
  <div class="top-band"></div>
  <div class="front-head">
    <h1 class="event-title">Fortbildungsveranstaltung<br>Krankenhaus Berlin</h1>
    <p class="event-topic">Neues aus der Schulter- und Kniearthroskopie</p>
  </div>
  <div class="year-divider">
    <svg width="396" height="30" viewBox="0 0 396 30" aria-hidden="true">
      <polygon points="273,0 396,0 396,30 0,30 0,21 255,21" fill="#3b3b3e"/>
    </svg>
    <span class="year-label">2019</span>
  </div>
  <div class="joint-visual" role="img" aria-label="Röntgenartige Darstellung eines Kniegelenks mit rot hervorgehobener Gelenkregion auf dunkelblauem Grund"></div>
  <div class="date-badge">
    <p class="date-badge__dates">21. 02. -<br>23. 02. 2019</p>
    <p class="date-badge__name">Veltrana-Symposium</p>
  </div>
  <div class="bottom-band"></div>
</section>

<section class="flyer flyer--back" aria-label="Rückseite">
  <div class="top-band"></div>
  <div class="photo-grid">
    <div class="photo photo--hand-light" role="img" aria-label="Helles Foto einer Hand"></div>
    <div class="photo photo--glove" role="img" aria-label="Foto einer Hand im medizinischen Handschuh"></div>
    <div class="photo photo--syringe" role="img" aria-label="Foto einer Spritze"></div>
    <div class="photo photo--shoulder" role="img" aria-label="Foto einer Hand, die eine Schulter abtastet"></div>
    <div class="back-heading">
      <p class="back-heading__kind">Fortbildungs-<br>veranstaltungen</p>
      <p class="back-heading__name">Veltrana-Symposium</p>
    </div>
  </div>
  <div class="joint-visual--soft" role="img" aria-label="Blasse, aufgehellte Darstellung eines Kniegelenks als Hintergrund"></div>
  <div class="year-divider">
    <svg width="396" height="30" viewBox="0 0 396 30" aria-hidden="true">
      <polygon points="273,0 396,0 396,30 0,30 0,21 255,21" fill="#3b3b3e"/>
    </svg>
    <span class="year-label">2019</span>
  </div>
  <div class="topic-badge">
    <p>Neues<br>aus der Schulter-<br>und<br>Kniearthroskopie</p>
  </div>
  <div class="teaser">
    <p class="teaser__lead">Lorem ipsum dolor sit</p>
    <p>amet, consetetur sadipscing elitr,<br>diam nonumy eirmod tempor</p>
  </div>
  <div class="info-band">
    <p>Für nähere Informationen:</p>
    <p>www.kursportal-muster.de</p>
  </div>
  <div class="bottom-band"></div>
</section>

</body>
</html>
```